Modern card design needed for building development company

We are looking for a sharp modern new look for our business cards.
We are a New Zealand based company called TKV Ventures NZ LTD that specialises in subdividing large sections, housing and commercial buildings.
We have attached a photo of the current logo and would like to see it improved somehow as it looks a bit dated.
We are open to any colours.

Target Market(s)

Investors, Property buyers

Industry/Entity Type

Investment

Contact Information for Business Card

TKV VENTURES NZ LTD
www.tkvventuresnz.co.nz

Howard Pennick
Phone +64 21 843 192
Email hdpennick@fernmail.co.nz

Font styles to use
Serif
Sans Serif

Colors
0792cd
33a6d7
85cae6
6b449b
886aae
f04a50
ec1f27
f37122
f68d4d

Requirements
Must have
• Please try and make the logo more modern or if you have a similar one we would like to see it.

```html
<!DOCTYPE html>
<html lang="en">
<head>
<meta charset="utf-8">
<title>TKV Ventures NZ LTD – Business Card</title>
<link href="https://fonts.googleapis.com/css2?family=Open+Sans:wght@400;600&display=swap" rel="stylesheet">
<style>
  :root {
    --bg: #ededed;
    --card: #ffffff;
    --brand-red: #a3121c;
    --name-blue: #1d4f9c;
    --band: #3b3b3d;
    --ink: #3a3a3a;
    --rule: #5a5a5a;
    --mark: #e6e4e2;
    --strip-a: #c3121c;
    --strip-b: #e0197d;
    --frame-orange: #f7a43a;
    --frame-yellow: #fde86a;
    --frame-pink: #f49ac1;
  }
  * { box-sizing: border-box; margin: 0; padding: 0; }
  html, body { width: 1200px; height: 873px; overflow: hidden; }
  body {
    background: var(--bg);
    font-family: "Open Sans", sans-serif;
    display: flex;
    align-items: center;
    justify-content: center;
    gap: 40px;
  }
  .card {
    position: relative;
    width: 540px;
    height: 310px;
    background: var(--card);
    box-shadow: 0 6px 18px rgba(0,0,0,.18);
    overflow: hidden;
  }

  /* Front */
  .brand-mark {
    position: absolute;
    left: 60px;
    top: 26px;
    display: flex;
    align-items: center;
    gap: 8px;
  }
  .brand-mark__square {
    width: 44px;
    height: 44px;
    background: var(--mark);
  }
  .brand-mark__name {
    font-size: 12px;
    font-weight: 600;
    color: var(--brand-red);
  }
  .company {
    position: absolute;
    right: 0;
    top: 38px;
    width: 240px;
    border-bottom: 1px solid var(--rule);
    padding-bottom: 4px;
    font-size: 17px;
    color: var(--brand-red);
    letter-spacing: .2px;
  }
  .contacts {
    position: absolute;
    left: 300px;
    top: 78px;
    list-style: none;
    font-size: 10px;
    color: var(--ink);
  }
  .contacts li {
    display: flex;
    align-items: center;
    gap: 8px;
    height: 24px;
  }
  .contacts .icon {
    width: 18px;
    height: 18px;
    flex: none;
  }
  .contacts .email { color: var(--name-blue); }
  .person {
    position: absolute;
    left: 244px;
    top: 160px;
    font-size: 30px;
    color: var(--name-blue);
    white-space: nowrap;
  }
  .tagline {
    position: absolute;
    left: 0;
    right: 0;
    bottom: 44px;
    height: 40px;
    background: var(--band);
    color: #fff;
    font-size: 11px;
    letter-spacing: .3px;
    display: flex;
    align-items: center;
    justify-content: center;
  }
  .accent-strip {
    position: absolute;
    left: 0;
    right: 0;
    bottom: 30px;
    height: 14px;
    background: linear-gradient(90deg, var(--strip-a) 0%, var(--strip-a) 55%, var(--strip-b) 85%, var(--strip-a) 100%);
  }

  /* Back */
  .back-frame {
    position: absolute;
    inset: 0;
    background: linear-gradient(135deg, var(--frame-pink) 0%, var(--frame-orange) 35%, var(--frame-orange) 55%, var(--frame-yellow) 80%, var(--frame-pink) 100%);
  }
  .back-inner {
    position: absolute;
    inset: 24px;
    background: var(--card);
    display: flex;
    align-items: center;
    justify-content: center;
    gap: 12px;
  }
  .back-inner .brand-mark__square { width: 70px; height: 70px; }
  .back-inner .brand-mark__name { font-size: 16px; }
</style>
</head>
<body>
  <section class="card card--front">
    <div class="brand-mark">
      <div class="brand-mark__square"></div>
      <span class="brand-mark__name">TKV Ventures</span>
    </div>
    <h1 class="company">TKV VENTURES NZ LTD</h1>
    <ul class="contacts">
      <li>
        <svg class="icon" viewBox="0 0 18 18" aria-hidden="true">
          <circle cx="9" cy="9" r="9" fill="#3b3b3d"/>
          <circle cx="9" cy="9" r="5" fill="none" stroke="#fff" stroke-width="1"/>
          <ellipse cx="9" cy="9" rx="2.2" ry="5" fill="none" stroke="#fff" stroke-width="1"/>
          <line x1="4" y1="9" x2="14" y2="9" stroke="#fff" stroke-width="1"/>
        </svg>
        <span>www.tkvventuresnz.co.nz</span>
      </li>
      <li>
        <svg class="icon" viewBox="0 0 18 18" aria-hidden="true">
          <circle cx="9" cy="9" r="9" fill="#3b3b3d"/>
          <path d="M6 4.5c.6-.4 1.2-.3 1.5.2l.8 1.5c.2.5.1 1-.3 1.3l-.6.4c.5 1.2 1.4 2.1 2.6 2.6l.4-.6c.3-.4.8-.5 1.3-.3l1.5.8c.5.3.6.9.2 1.5-.6.9-1.6 1.3-2.6 1-2.8-.9-4.9-3-5.8-5.8-.3-1 .1-2 1-2.6z" fill="#fff"/>
        </svg>
        <span>+64 21 843 192</span>
      </li>
      <li class="email"><span>hdpennick@fernmail.co.nz</span></li>
    </ul>
    <p class="person">Howard Pennick</p>
    <p class="tagline">SUBDIVIDING LARGE SECTIONS, HOUSING AND COMMERCIAL BUILDINGS</p>
    <div class="accent-strip" role="img" aria-label="Red and magenta checkered accent strip"></div>
  </section>

  <section class="card card--back">
    <div class="back-frame" role="img" aria-label="Colourful orange, yellow and pink mosaic border"></div>
    <div class="back-inner">
      <div class="brand-mark__square"></div>
      <span class="brand-mark__name">TKV Ventures</span>
    </div>
  </section>
</body>
</html>
```